Holvern Incorporated

Holvern is a business that provides consulting, and manages and supplies trades persons in the construction and heavy industries sector. We build, do maintenance, install machinery, and can manage projects or jobs. Would like or prefer more clean, classic designs. Blacks/greys, but open to almost anything.

Target Market(s)

Industrial/Construction/Manufacturing

Industry/Entity Type

Construction Company

Contact Information for Business Card

Clean, business name on the front, possibly have the details on the back, but open to any ideas.

Logo Text

We currently do not have a slogan, open to ideas

Font styles to use
Serif
Sans Serif

Colors

Designer to choose colors to be used in the design.

Requirements
Should not have
• the oval is not my logo, was just an idea. please don't send 20 designs with the oval

```html
<!DOCTYPE html>
<html lang="en">
<head>
<meta charset="utf-8">
<title>Holvern Incorporated – Business Card</title>
<link href="https://fonts.googleapis.com/css2?family=Bitter:wght@600&family=Montserrat:wght@400;600;700&display=swap" rel="stylesheet">
<style>
  :root {
    --page: #f0efec;
    --card-black: #0a0b0a;
    --card-white: #ffffff;
    --band-grey: #e0e1dd;
    --ink: #2a2a2a;
    --rule: #5a5a5a;
    --logo-white: #ffffff;
  }
  * { margin: 0; padding: 0; box-sizing: border-box; }
  html, body { width: 1200px; height: 1000px; overflow: hidden; }
  body {
    background: var(--page);
    position: relative;
    font-family: "Montserrat", sans-serif;
    color: var(--ink);
  }
  .card {
    position: absolute;
    left: 226px;
    width: 747px;
    height: 447px;
    box-shadow: 5px 5px 6px rgba(0,0,0,0.35);
  }
  .card-front { top: 38px; background: var(--card-black); }
  .card-back { top: 518px; background: var(--card-white); }

  .brand {
    position: absolute;
    left: 0; right: 0;
    top: 150px;
    text-align: center;
    font-family: "Bitter", serif;
    font-weight: 600;
    color: var(--logo-white);
  }
  .brand-name { font-size: 104px; line-height: 1; letter-spacing: 1px; }
  .brand-suffix {
    font-size: 17px;
    letter-spacing: 1px;
    text-align: right;
    width: 524px;
    margin: 6px auto 0;
  }

  .job-title {
    position: absolute;
    top: 58px; left: 0; right: 0;
    text-align: center;
    font-size: 11.5px;
    letter-spacing: 0.35em;
  }
  .person-name {
    position: absolute;
    top: 84px; left: 0; right: 0;
    text-align: center;
    font-size: 25px;
    font-weight: 700;
    letter-spacing: 0.62em;
    padding-left: 0.62em;
  }
  .contact-band {
    position: absolute;
    top: 142px; left: 0;
    width: 100%; height: 236px;
    background: var(--band-grey);
  }
  .rule {
    position: absolute;
    left: 136px; width: 473px;
    height: 1px; background: var(--rule);
  }
  .band-line {
    position: absolute;
    left: 0; right: 0;
    text-align: center;
    font-size: 11px;
  }
  .col-divider {
    position: absolute;
    left: 373px; top: 47px;
    width: 1px; height: 94px;
    background: var(--rule);
  }
  .contact-col {
    position: absolute;
    top: 68px;
    font-size: 11px;
    line-height: 22px;
  }
  .contact-col h3 { font-size: 11px; font-weight: 600; }
  .contact-email { right: 400px; text-align: right; }
  .contact-phone { left: 400px; text-align: left; }
  .social {
    position: absolute;
    top: 191px; left: 0; right: 0;
    display: flex; justify-content: center; gap: 4px;
  }
  .social-dot {
    width: 21px; height: 21px;
    border: 1.5px solid var(--ink);
    border-radius: 50%;
  }
</style>
</head>
<body>
  <section class="card card-front">
    <div class="brand">
      <div class="brand-name">Holvern</div>
      <div class="brand-suffix">INCORPORATED</div>
    </div>
  </section>

  <section class="card card-back">
    <p class="job-title">- OPERATIONAL DIRECTOR -</p>
    <h1 class="person-name">DANIEL ASHWORTH</h1>
    <div class="contact-band">
      <div class="rule" style="top:22px"></div>
      <p class="band-line" style="top:28px">Your Company Adress</p>
      <div class="rule" style="top:52px"></div>
      <div class="col-divider"></div>
      <div class="contact-col contact-email">
        <h3>E-Mail</h3>
        <p>your@email.com</p>
        <p>www.yourwebsite.com</p>
      </div>
      <div class="contact-col contact-phone">
        <h3>Phone</h3>
        <p>00 (123) 4567 890 (Fax)</p>
        <p>00 (715) 8521 000 (Mobile)</p>
      </div>
      <div class="rule" style="top:146px"></div>
      <p class="band-line" style="top:153px">Let’s keep in touch, Follow Us on Social Media</p>
      <div class="rule" style="top:178px"></div>
      <div class="social" aria-label="Social media links">
        <span class="social-dot"></span>
        <span class="social-dot"></span>
        <span class="social-dot"></span>
        <span class="social-dot"></span>
        <span class="social-dot"></span>
      </div>
    </div>
  </section>
</body>
</html>
```